New one page Homepage with registration and log in form

Hi designers!

We need a new homepage and made a skitch of how it should be.

Can you give some of your design ideas and work it out so that it actually looks great?

Its just one page, for convertion reasons.

The logo doesnt have to be changed.

It would be cool to center the logo but not sure how design technically correct that is.

The social icons can be left out.

If you could give a few mockups than we can choose the best one.

I added one screenshot sketch of the homepage.

And 2 screenshots of what the system looks like on the inside, just so you get an idea.

Thanks

Target Market(s)

Vacation rental owners who want to increase their bookings by connecting with other VR owners and managers, or by having their own booking team for a small fee.

Industry/Entity Type

Social

Number of Pages Required

1 page

Requirements
Must have
• Use your imagination please
Nice to have
• Use your imagination
• It will be a one page design so we need to impress :)
• Keep it compact, maybe a web 3.0 flat design, etc
Should not have
• Other pages.

```html
<!DOCTYPE html>
<html lang="en">
<head>
<meta charset="utf-8">
<title>StayCircle – The First Social Booking Network</title>
<link href="https://fonts.googleapis.com/css2?family=Ubuntu:wght@400;500;700&display=swap" rel="stylesheet">
<style>
:root{
  --blue-deep:#0a4f97;
  --blue-mid:#2f86cf;
  --sky:#9fd0f0;
  --ink:#3a3a3a;
  --muted:#777;
  --line:#d6d6d6;
  --white:#fff;
  --orange-a:#ffb000;
  --orange-b:#ff8400;
  --green-a:#22b04f;
  --green-b:#14a043;
  --social:#0e4fa8;
  --footer-bar:#eeeeee;
  --round-a:#3a5a98;
  --round-b:#3d9ad8;
  --round-c:#d8322b;
}
*{box-sizing:border-box;margin:0;padding:0}
html,body{width:1200px;height:1171px;overflow:hidden}
body{position:relative;font-family:"Ubuntu",sans-serif;color:var(--ink);background:#f3f3f3}
.abs{position:absolute}
.header{left:0;top:0;width:1200px;height:97px;background:linear-gradient(#fff,#f1f1f1)}
.brand{left:112px;top:28px;font-size:26px;font-weight:700;color:var(--blue-deep);display:flex;align-items:center;gap:8px}
.brand i{width:14px;height:14px;border-radius:50%;background:var(--orange-b);display:block}
.follow-top{right:110px;top:11px;display:flex;align-items:center;gap:6px;font-size:12px;color:#666}
.dot{width:25px;height:25px;border-radius:50%;display:inline-block}
.d1{background:var(--round-a)}.d2{background:var(--round-b)}.d3{background:var(--round-c)}
.login-btn{left:1003px;top:54px;width:87px;height:28px;border:1px solid #ccc;border-radius:3px;background:#fff;font-size:12px;color:#555;display:flex;align-items:center;justify-content:center;gap:7px}
.hero{left:0;top:97px;width:1200px;height:680px;background:linear-gradient(180deg,var(--blue-deep) 0%,var(--blue-mid) 45%,var(--sky) 68%,#f3f3f3 100%)}
.hero-line{left:0;top:503px;width:1200px;height:5px;border-top:1px solid rgba(255,255,255,.45);border-bottom:1px solid rgba(255,255,255,.45)}
.title{left:0;top:122px;width:1200px;text-align:center;color:#fff;font-size:26px;font-weight:500}
.video{left:110px;top:178px;width:493px;height:297px;background:#fff;border-radius:3px}
.pitch{left:623px;top:173px;width:468px;color:#fff;font-size:14px;line-height:23px;text-shadow:0 1px 1px rgba(0,0,0,.2)}
.pitch p{margin-bottom:23px}
.pitch u{text-decoration:none;border-bottom:1px solid rgba(255,255,255,.7)}
.panel{top:532px;height:451px;background:#fff;border-radius:3px;box-shadow:0 0 3px rgba(0,0,0,.12)}
.panel h2{position:absolute;left:0;width:100%;top:22px;text-align:center;font-size:21px;font-weight:500;color:#333}
.field{position:absolute;height:37px;border:1px solid var(--line);border-radius:3px;font-size:12.5px;color:#555;padding:0 17px;display:flex;align-items:center;background:#fff}
.btn{position:absolute;border-radius:3px;color:#fff;font-size:18px;font-weight:500;display:flex;align-items:center;justify-content:center}
.btn-login{left:32px;top:216px;width:430px;height:52px;background:linear-gradient(var(--orange-a),var(--orange-b))}
.btn-reg{left:24px;top:369px;width:430px;height:53px;background:linear-gradient(var(--green-a),var(--green-b))}
.small{position:absolute;left:0;width:100%;text-align:center;font-size:12.5px}
.btn-social{left:133px;top:342px;width:228px;height:42px;background:var(--social);font-size:13px;font-weight:400;justify-content:flex-start;padding-left:56px}
.check{position:absolute;left:32px;top:178px;width:24px;height:24px;border:1px solid var(--line);border-radius:3px}
.footer{left:0;top:1002px;width:1200px;height:133px;background:#fff;border-top:1px solid #e3e3e3}
.footer h3{position:absolute;top:14px;font-size:14px;font-weight:500;color:#333}
.col{position:absolute;top:41px;font-size:11.5px;line-height:21px;color:#444;list-style:none}
.bar{left:0;top:1135px;width:1200px;height:36px;background:var(--footer-bar);border-top:1px solid #ddd;font-size:11.5px;color:#444;text-align:center;line-height:34px}
</style>
</head>
<body>
<header class="abs header"></header>
<div class="abs brand"><i></i>StayCircle</div>
<div class="abs follow-top">Follow Us <span class="dot d1"></span><span class="dot d2"></span><span class="dot d3"></span></div>
<div class="abs login-btn">
  <svg width="11" height="11" viewBox="0 0 11 11"><circle cx="5.5" cy="3" r="2.6" fill="#777"/><path d="M0 11c0-3.5 2.5-4.5 5.5-4.5S11 7.5 11 11z" fill="#777"/></svg>
  Login
  <svg width="9" height="6" viewBox="0 0 9 6"><path d="M0 0h9L4.5 6z" fill="#888"/></svg>
</div>

<section class="abs hero" role="img" aria-label="Blue sky fading into soft white clouds"></section>
<div class="abs hero-line"></div>
<h1 class="abs title">The First Social Booking Network</h1>

<div class="abs video">
  <svg width="493" height="297" viewBox="0 0 493 297">
    <circle cx="246" cy="132" r="57" fill="none" stroke="#c6c6c6" stroke-width="10"/>
    <path d="M228 104v56l45-28z" fill="#c6c6c6"/>
    <rect x="12" y="254" width="469" height="25" fill="#666"/>
    <rect x="12" y="254" width="37" height="25" fill="#0d4ea0"/>
    <path d="M26 260v13l11-6.5z" fill="#fff"/>
    <rect x="58" y="262" width="390" height="9" fill="#fff"/>
    <rect x="58" y="262" width="47" height="9" fill="#aaa"/>
    <rect x="452" y="254" width="29" height="25" fill="#0d4ea0"/>
    <rect x="460" y="259" width="13" height="11" fill="none" stroke="#fff" stroke-width="1.3"/>
    <path d="M465 264l8 7" stroke="#fff" stroke-width="1.3"/>
  </svg>
</div>

<div class="abs pitch">
  <p>StayCircle is a new <u>Social Booking Network</u>.<br>Vacation Rental hosts and property Managers can find each other connect and chat amongst themselves for sharing reservation inquiries, services or anything you can imagine, in a convenient social enviorement.</p>
  <p>The Social Booking Network is absolutely FREE. Howeaver if you want to save time and get really professional about increasing your bookingss. Than you should consider having your own Booking Team.</p>
  <p>For just 2.5% your own StayCircle hosts take care of all tedious online reservation management tasks for ou in the most advanced, personalized and professional way possible.</p>
</div>

<section class="abs panel" style="left:110px;width:493px">
  <h2>Login to your account</h2>
  <div class="field" style="left:32px;top:78px;width:430px">Your username or email address</div>
  <div class="field" style="left:32px;top:130px;width:430px">Your password</div>
  <div class="check"></div>
  <div class="small" style="left:67px;top:183px;width:auto;text-align:left;color:#444">Would you like us to remember you?</div>
  <div class="btn btn-login">LOG ME IN</div>
  <div class="small" style="top:313px;font-weight:500;color:#333">Sign in with your social identity</div>
  <div class="btn btn-social">Sign in with Linkup</div>
  <div class="small" style="top:398px;color:var(--muted)">I forget my username / password</div>
</section>

<section class="abs panel" style="left:619px;width:471px">
  <h2>Don’t have an account</h2>
  <div class="small" style="top:50px;font-size:11.5px;color:#555">Register now to join the Free Booking Network!</div>
  <div class="field" style="left:23px;top:78px;width:211px">First Name</div>
  <div class="field" style="left:243px;top:78px;width:209px">Last Name</div>
  <div class="field" style="left:23px;top:128px;width:429px">Username</div>
  <div class="field" style="left:23px;top:177px;width:429px">Password</div>
  <div class="field" style="left:23px;top:224px;width:429px">user@mailbox.com</div>
  <div class="field" style="left:23px;top:271px;width:429px">Your Contact Number Ex. +12586778896</div>
  <div class="field" style="left:23px;top:319px;width:429px">Whats your reason for joining?</div>
  <div class="btn btn-reg">REGISTER</div>
</section>

<footer class="abs footer">
  <h3 style="left:110px">ABOUT US</h3>
  <ul class="col" style="left:110px"><li>Home</li><li>About Us</li><li>Contact</li><li>Circle Book</li></ul>
  <ul class="col" style="left:296px"><li>Calendar</li><li>Properties</li><li>Contact Us</li></ul>
  <ul class="col" style="left:490px"><li>Disclaimer</li><li>Sitemap</li><li>Privacy Policy</li></ul>
  <ul class="col" style="left:731px"><li>Automations</li><li>Channels</li><li>Tools</li></ul>
  <h3 style="left:890px">FOLLOW US</h3>
  <div class="abs" style="left:890px;top:40px;display:flex;gap:7px"><span class="dot d1"></span><span class="dot d2"></span><span class="dot d3"></span></div>
</footer>
<div class="abs bar">Copyright © 2014 Staycircle.com. All Rights Reserved.</div>
</body>
</html>
```